Business Card

Harbourline Athletics ([url removed, login to view]) develops fundraising software for not for profit sporting clubs/teams.

We launched only 12 months ago and ran limited beta testing software to ensure the quality of the software. Coming into the 2018 winter season we are ready to ramp it up.

As we are a new company the business card will need to show that we are trustworthy, a serious business and larger than we look. I am also looking for consistency within the brand.

The major fundraising software we will be running next year will be Lantern Play ([url removed, login to view]) which is a Tipping Competition for a number of sporting leagues in Australia.

Harbourline Athletics is the name of the company that should be the major focus but there should also be a secondary focus on Lantern Play (both logos are attached). I am happy to see suggestions of how this can work, either front and back differences or a combination, I am looking for suggestions from you.

I am thinking of a secondary catch line for Harbourline Athletics which is "Fundraising Software for Grass Roots Sport" which I would like to see incorporated.

Please add the following information (happy to see icons or other ways to display this info)

Name: Doug Pranley
Mobile: 0455 218 634 (i will give the number to the winner)
email: doug@[url removed, login to view]
Linked In - [url removed, login to view]
Web - [url removed, login to view]

If it works also having [url removed, login to view]

```html
<!DOCTYPE html>
<html lang="en">
<head>
<meta charset="utf-8">
<title>Harbourline Athletics – Business Card</title>
<link href="https://fonts.googleapis.com/css2?family=Ubuntu:wght@400;700&display=swap" rel="stylesheet">
<style>
  :root{
    --stage:#e9e9ea;
    --lime:#9cc43a;
    --navy:#1f3b8a;
    --red:#d9202e;
    --blue:#1f48a8;
    --white:#ffffff;
    --ink:#2b2b2b;
    --map-a:#e6ebf2;
    --map-b:#cfd9e6;
  }
  *{box-sizing:border-box;margin:0;padding:0}
  html,body{width:1200px;height:768px;overflow:hidden}
  body{background:var(--stage);font-family:"Ubuntu",sans-serif;position:relative}

  .card{position:absolute;top:241px;width:500px;height:286px;border-radius:4px;overflow:hidden;box-shadow:0 6px 18px rgba(0,0,0,.18)}
  .card--back{left:60px;background:var(--lime)}
  .card--front{left:640px;background:var(--white)}

  .brand{position:absolute;display:flex;align-items:center;gap:10px}
  .brand__dot{width:34px;height:34px;border-radius:50%;background:var(--navy);flex:none}
  .brand__name{font-weight:700;font-size:30px;color:var(--navy);line-height:1;white-space:nowrap}

  /* back */
  .card--back .brand{left:88px;top:104px}
  .card--back .web{position:absolute;right:22px;top:162px;font-size:11px;color:var(--navy)}

  .partner{position:absolute;display:flex;align-items:center;gap:7px}
  .partner__dot{width:22px;height:22px;border-radius:50%;background:var(--red);flex:none}
  .partner__name{font-weight:700;font-size:15px;color:var(--navy);white-space:nowrap}
  .card--back .partner{left:24px;bottom:26px}

  /* front */
  .map{position:absolute;left:150px;top:70px;width:250px;height:140px;border-radius:50%;background:radial-gradient(ellipse at center,var(--map-b),var(--map-a) 60%,rgba(255,255,255,0) 100%)}
  .bands{position:absolute;inset:0;width:100%;height:100%}

  .card--front .brand{right:22px;top:24px;gap:8px}
  .card--front .brand__dot{width:24px;height:24px}
  .card--front .brand__name{font-size:20px}

  .person{position:absolute;right:22px;top:70px;text-align:right}
  .person__name{font-size:17px;color:var(--ink);white-space:nowrap}
  .person__role{font-size:9px;letter-spacing:.12em;color:var(--ink);margin-top:2px}

  .contacts{position:absolute;right:22px;top:118px;list-style:none}
  .contacts li{display:flex;justify-content:flex-end;align-items:center;gap:8px;font-size:10.5px;color:var(--ink);height:21px;white-space:nowrap}
  .contacts svg{width:11px;height:11px;fill:var(--red);flex:none}

  .card--front .partner{left:40px;top:180px;flex-direction:column;align-items:flex-start;gap:3px}
  .partner__row{display:flex;align-items:center;gap:7px}
  .card--front .partner__name{font-size:16px;color:var(--ink)}
  .partner__web{font-size:8px;color:var(--ink);padding-left:29px;white-space:nowrap}
</style>
</head>
<body>

<section class="card card--back">
  <div class="brand">
    <span class="brand__dot"></span>
    <span class="brand__name">Harbourline Athletics</span>
  </div>
  <div class="web">www.lanternplay.com</div>
  <div class="partner">
    <span class="partner__dot"></span>
    <span class="partner__name">Lantern Play</span>
  </div>
</section>

<section class="card card--front">
  <div class="map" role="img" aria-label="Faint world map background"></div>
  <svg class="bands" viewBox="0 0 500 286" preserveAspectRatio="none" aria-hidden="true">
    <path d="M0,0 H140 Q35,55 0,170 Z" fill="#d9202e"/>
    <path d="M140,0 Q35,55 0,170" fill="none" stroke="#1f48a8" stroke-width="2"/>
    <path d="M0,250 L240,266 L256,286 H0 Z" fill="#1f48a8"/>
    <path d="M240,266 L500,248 V286 H256 Z" fill="#d9202e"/>
  </svg>

  <div class="brand">
    <span class="brand__dot"></span>
    <span class="brand__name">Harbourline Athletics</span>
  </div>

  <div class="person">
    <div class="person__name">DOUG PRANLEY</div>
    <div class="person__role">FOUNDER</div>
  </div>

  <ul class="contacts">
    <li>0455 218 634 <svg viewBox="0 0 24 24"><path d="M6.6 10.8a15 15 0 0 0 6.6 6.6l2.2-2.2a1 1 0 0 1 1-.25 11.4 11.4 0 0 0 3.6.57 1 1 0 0 1 1 1V20a1 1 0 0 1-1 1A17 17 0 0 1 3 4a1 1 0 0 1 1-1h3.5a1 1 0 0 1 1 1c0 1.25.2 2.45.57 3.57a1 1 0 0 1-.25 1z"/></svg></li>
    <li>doug@harbourlineathletics.com <svg viewBox="0 0 24 24"><path d="M2 5h20v14H2z"/><path d="M3 6l9 7 9-7" fill="none" stroke="#fff" stroke-width="2"/></svg></li>
    <li>www.proflink.net/in/dougpranley <svg viewBox="0 0 24 24"><rect x="3" y="3" width="18" height="18" rx="2"/></svg></li>
    <li>www.harbourlineathletics.com <svg viewBox="0 0 24 24"><circle cx="12" cy="12" r="9"/></svg></li>
  </ul>

  <div class="partner">
    <div class="partner__row">
      <span class="partner__dot"></span>
      <span class="partner__name">Lantern Play</span>
    </div>
    <span class="partner__web">www.harbourlineathletics.com</span>
  </div>
</section>

</body>
</html>
```